Flyer Advertisement Simple But Creative

Flyer dimensions 4" x 6"

Simple design with logo and additional info. On the front of the flyer:

- place the logo at the top
- beneath the logo add the website and phone number
- simple less is more approach
- feel free to add your own personal touch

On the back:

- Requirements
- Perfect for Birthdays and Anniversaries
- Rentals available hourly, daily, and weekly
- Group Rentals available at discounted rates
- Enter to win a free rental - url and QR code

Industry/Entity Type

Car Rental

Font styles to use
Serif
Sans Serif

Colors

Designer to choose colors to be used in the design.

Requirements
Must have
• FRONT:
• Please include our phone number and website:
• 614-287-3951
• www.BrindlewoodTrikeHire.example
• BACK:
• REQUIREMENTS
• At least 25 years of age
• Valid Driver's License
• Debit or Credit Card
• Must know how to drive a manual transmission or stick shift

```html
<!DOCTYPE html>
<html lang="en">
<head>
<meta charset="utf-8">
<title>Brindlewood Trike Hire – Flyer</title>
<link rel="stylesheet" href="https://fonts.googleapis.com/css2?family=Oswald:wght@600&family=Arimo:wght@400&family=Roboto+Condensed:wght@300&display=swap">
<style>
  :root {
    --stage: #2a2a2a;
    --paper: #ffffff;
    --brand-red: #ee1c4f;
    --ink: #111111;
    --art-grey: #b9bec3;
    --art-dark: #2b2d31;
  }
  * { box-sizing: border-box; margin: 0; padding: 0; }
  html, body { width: 1200px; height: 1000px; overflow: hidden; background: var(--stage); }
  .canvas { position: relative; width: 1200px; height: 1000px; }
  .card {
    position: absolute; top: 125px; width: 500px; height: 750px;
    background: var(--paper); overflow: hidden;
    box-shadow: 0 4px 14px rgba(0,0,0,.45);
  }
  .card--front { left: 74px; }
  .card--back { left: 622px; }

  /* Front */
  .hero-art {
    position: absolute; left: 66px; top: 55px; width: 360px; height: 305px;
    border-radius: 50%;
    background: radial-gradient(circle at 55% 50%, var(--art-dark) 0 28%, var(--brand-red) 29% 36%, var(--art-grey) 37% 70%, rgba(185,190,195,0) 71%);
  }
  .brand-name {
    position: absolute; left: 0; right: 0; top: 368px; text-align: center;
    font-family: "Oswald", sans-serif; font-weight: 600; font-size: 30px;
    letter-spacing: 1px; color: var(--ink); text-transform: uppercase;
  }
  .brand-rule {
    position: absolute; left: 118px; width: 274px; top: 423px; height: 1px; background: var(--brand-red);
  }
  .contact-heading {
    position: absolute; left: 0; top: 488px; width: 500px; height: 63px;
    background: var(--brand-red); color: var(--paper); text-align: center;
    font-family: "Oswald", sans-serif; font-weight: 600; font-size: 34px; line-height: 60px;
  }
  .contact-body {
    position: absolute; left: 0; top: 560px; width: 500px; height: 190px;
    background: var(--brand-red); color: var(--paper); text-align: center;
  }
  .contact-phone {
    margin-top: 42px; font-family: "Oswald", sans-serif; font-weight: 600; font-size: 28px;
  }
  .contact-web {
    margin-top: 22px; font-family: "Arimo", sans-serif; font-size: 22px;
  }

  /* Back */
  .band {
    position: absolute; left: 0; width: 500px; height: 62px; background: var(--brand-red);
    color: var(--paper); padding-left: 45px;
    font-family: "Oswald", sans-serif; font-weight: 600; font-size: 32px; line-height: 60px;
  }
  .band--title { top: 50px; }
  .band--requirements { top: 373px; }
  .perk-list, .rule-list { position: absolute; left: 0; list-style: none; }
  .perk-list { top: 142px; }
  .perk {
    position: relative; padding-left: 91px; height: 61px;
    font-family: "Arimo", sans-serif; font-size: 18px; color: var(--ink); line-height: 28px;
  }
  .perk svg { position: absolute; left: 43px; top: 0; }
  .perk-note {
    position: absolute; left: 91px; top: 316px;
    font-family: "Roboto Condensed", sans-serif; font-weight: 300; font-size: 19px; color: var(--ink);
  }
  .perk-note span { color: var(--brand-red); }
  .rule-list { top: 476px; }
  .rule {
    position: relative; padding-left: 84px; margin-bottom: 36px; width: 420px;
    font-family: "Arimo", sans-serif; font-size: 18px; color: var(--ink); line-height: 23px;
  }
  .rule::before {
    content: ""; position: absolute; left: 48px; top: 5px; width: 9px; height: 9px;
    border-radius: 50%; background: var(--brand-red);
  }
</style>
</head>
<body>
<main class="canvas">
  <section class="card card--front">
    <div class="hero-art" role="img" aria-label="Illustration of a red and black three-wheeled roadster on grey brush strokes"></div>
    <div class="brand-name">Brindlewood Trike Hire</div>
    <div class="brand-rule"></div>
    <div class="contact-heading">Contact Us</div>
    <div class="contact-body">
      <p class="contact-phone">614-287-3951</p>
      <p class="contact-web">www.BrindlewoodTrikeHire.example</p>
    </div>
  </section>

  <section class="card card--back">
    <h2 class="band band--title">Brindlewood Trike Hire</h2>
    <ul class="perk-list">
      <li class="perk"><svg width="24" height="24" viewBox="0 0 24 24"><rect x="2" y="4" width="17" height="17" fill="none" stroke="#ee1c4f" stroke-width="3"/><path d="M6 12l4 4 11-13" fill="none" stroke="#ee1c4f" stroke-width="3"/></svg>Perfect for Birthdays and Anniversaries</li>
      <li class="perk"><svg width="24" height="24" viewBox="0 0 24 24"><rect x="2" y="4" width="17" height="17" fill="none" stroke="#ee1c4f" stroke-width="3"/><path d="M6 12l4 4 11-13" fill="none" stroke="#ee1c4f" stroke-width="3"/></svg>Rentals available hourly, daily, and weekly</li>
      <li class="perk"><svg width="24" height="24" viewBox="0 0 24 24"><rect x="2" y="4" width="17" height="17" fill="none" stroke="#ee1c4f" stroke-width="3"/><path d="M6 12l4 4 11-13" fill="none" stroke="#ee1c4f" stroke-width="3"/></svg>Group Rentals available at discounted rates</li>
    </ul>
    <p class="perk-note"><span>*</span>Enter to win a free rental - url and QR code</p>
    <h2 class="band band--requirements">Requirements</h2>
    <ul class="rule-list">
      <li class="rule">At least 25 years of age.</li>
      <li class="rule">A Valid Driver's License.</li>
      <li class="rule">Debit or Credit Card.</li>
      <li class="rule">Must know how to drive a manual transmission or stick shift</li>
    </ul>
  </section>
</main>
</body>
</html>
```